1923 Basins & Spouts Business Card

I'm wanting to get a business card designed. Our business is 1923 Basins & Spouts
Details for the card:

1923 Basins & Spouts
Name: Gareth Vostle
Email: gareth@1923basinsandspouts.com.au
Website: www.1923basinsandspouts.com.au
Mobile: 0491 570 158
Phone: 02 5550 1843

Font of Basins & Spouts is called Snell Roundhand. Not sue what font logo text is.

I'm thinking two sided but it doesn't have to be.

```html
<!DOCTYPE html>
<html lang="en">
<head>
<meta charset="utf-8">
<title>1923 Basins &amp; Spouts — Business Card</title>
<link rel="stylesheet" href="https://fonts.googleapis.com/css2?family=Great+Vibes&family=Josefin+Sans:wght@300;400&family=Open+Sans:wght@400&display=swap">
<style>
  :root {
    --backdrop: #eeeef0;
    --card-front: #ffffff;
    --card-back: #b96e78;
    --ink: #161414;
    --ink-soft: #3a3535;
    --cream: #fbeef0;
    --frame-line: #f3d9dd;
  }
  * { box-sizing: border-box; margin: 0; padding: 0; }
  html, body {
    width: 1200px; height: 895px; overflow: hidden;
    background: var(--backdrop);
  }
  .canvas { position: relative; width: 1200px; height: 895px; }

  .card {
    position: absolute;
    width: 470px; height: 262px;
    box-shadow: 0 6px 18px rgba(60, 40, 45, 0.12);
  }

  /* Front */
  .card-front { left: 190px; top: 185px; background: var(--card-front); }
  .brand {
    position: absolute; left: 0; right: 0; top: 92px;
    text-align: center;
  }
  .brand-name {
    display: block;
    font-family: "Great Vibes", cursive;
    font-size: 44px; line-height: 1; color: var(--ink);
    white-space: nowrap;
  }
  .tagline {
    margin-top: 12px;
    font-family: "Open Sans", sans-serif;
    font-size: 11px; color: var(--ink-soft); letter-spacing: 0.1px;
    white-space: nowrap;
  }

  /* Back */
  .card-back { left: 540px; top: 450px; background: var(--card-back); }
  .card-frame { position: absolute; inset: 0; }
  .holder-name {
    position: absolute; top: 46px; left: 0; right: 0; text-align: center;
    font-family: "Great Vibes", cursive; font-weight: 400;
    font-size: 38px; line-height: 1.2; color: var(--cream);
  }
  .contact-list {
    position: absolute; top: 118px; left: 0; right: 0;
    margin: 0 auto; width: max-content;
    display: grid; grid-template-columns: auto auto; column-gap: 8px; row-gap: 3px;
    font-family: "Josefin Sans", sans-serif; font-weight: 300;
    font-size: 14px; color: var(--cream);
  }
  .contact-list dt { text-align: right; }
  .contact-list dd { white-space: nowrap; }
</style>
</head>
<body>
<main class="canvas">

  <section class="card card-front" aria-label="Business card front">
    <div class="brand">
      <span class="brand-name">1923 Basins &amp; Spouts</span>
      <p class="tagline">Classic elegance shaped for everyday living</p>
    </div>
  </section>

  <section class="card card-back" aria-label="Business card back">
    <svg class="card-frame" viewBox="0 0 470 262" aria-hidden="true">
      <g fill="none" stroke="var(--frame-line)" stroke-width="1.2">
        <line x1="14" y1="28" x2="456" y2="28"/>
        <line x1="14" y1="234" x2="456" y2="234"/>
        <line x1="22" y1="20" x2="22" y2="242"/>
        <line x1="448" y1="20" x2="448" y2="242"/>
        <rect x="30" y="36" width="410" height="190"/>
      </g>
    </svg>
    <h1 class="holder-name">Gareth Vostle</h1>
    <dl class="contact-list">
      <dt>Email:</dt><dd>gareth@1923basinsandspouts.com.au</dd>
      <dt>Website:</dt><dd>www.1923basinsandspouts.com.au</dd>
      <dt>Mobile:</dt><dd>0491 570 158</dd>
      <dt>Phone:</dt><dd>02 5550 1843</dd>
    </dl>
  </section>

</main>
</body>
</html>
```